Poster for Starlette-style Christmas music and dance show.

I need a poster for a Christmas music and dance show styled after the Harbor Lane Starlettes. Attached are samples of posters for previous years. I like the font style and colors of the blue one. The design should contain an ornament design with dancers dancing on it. The dancers should be cartoon style, not photo real. A sample is attached.
The poster MUST contain the PelMUSE logo, sponsor logos, the dates (December 12-13, 2015), the location (Lyle & Ruth Danvers Theatre, 4817 Quillberry Bend, Lakeway, TX), PelMUSE contact info (www.pel-muse.example and 555-307-4162 ext 204), and "Directed and Choreographed by Colin Ashby."
Logos are all attached. Finalized files needed in sizes: 12x18, 4x6, and 30x48 inches.

Target Market(s)

Community Theatre patrons

Industry/Entity Type

Radio

Font styles to use
Serif

Colors
0792cd
33a6d7
85cae6
ecf7fb
ffffff

Requirements
Must have
• PelMUSE logo (attached)
• sponsor logos: Neva Orr Photography, Pruitt Dentistry, Bluefin Grill, Up Tempo (attached)
• Show dates: December 12-13, 2015)
• Show Location: Lyle & Ruth Danvers Theatre, 4817 Quillberry Bend, Lakeway, TX)
• PelMUSE contact info: www.pel-muse.example and 555-307-4162 ext 204
• "Directed and Choreographed by Colin Ashby"
• An ornament design with dancers on it. The dancers should be cartoon style, not photo real. A sample of a dancer graphic is attached.
Nice to have
• snowflakes or other winter themes

```html
<!DOCTYPE html>
<html lang="en">
<head>
<meta charset="utf-8">
<title>Holiday Extravaganza – PelMUSE Broadway Company</title>
<link rel="stylesheet" href="https://fonts.googleapis.com/css2?family=Lobster&family=Kaushan+Script&family=Playfair+Display:wght@400;700&family=Oswald:wght@500;700&family=Libre+Baskerville:ital@0;1&display=swap">
<style>
  :root {
    --night-purple: #2c1466;
    --deep-violet: #4a2a9a;
    --royal-blue: #2f5fc9;
    --ice-blue: #85cae6;
    --frost: #ecf7fb;
    --white: #ffffff;
    --holiday-red: #d8191c;
    --gold: #f3c13a;
    --gold-deep: #c98a12;
    --sponsor-dark: #1d0f44;
  }
  * { margin: 0; padding: 0; box-sizing: border-box; }
  html, body { width: 753px; height: 1200px; overflow: hidden; }
  body { background: var(--night-purple); }

  .poster {
    position: relative;
    width: 753px;
    height: 1200px;
    overflow: hidden;
    color: var(--white);
    font-family: "Playfair Display", Georgia, serif;
  }
  .poster p, .poster h1, .poster h2 { white-space: nowrap; }

  .winter-backdrop {
    position: absolute; inset: 0;
    background:
      radial-gradient(ellipse 70% 35% at 50% 28%, rgba(133,202,230,.35), transparent 70%),
      linear-gradient(180deg, var(--royal-blue) 0%, var(--deep-violet) 22%, var(--night-purple) 50%, var(--deep-violet) 74%, var(--ice-blue) 94%, var(--frost) 100%);
  }

  .academy-mark {
    position: absolute; top: 18px; left: 238px; width: 277px; height: 84px;
    background: var(--white);
    border-radius: 0 0 22px 22px;
    display: flex; align-items: center; justify-content: center;
    color: var(--deep-violet);
    font-family: "Playfair Display", Georgia, serif;
    font-weight: 700; font-size: 30px; line-height: 1;
    white-space: nowrap;
  }

  .company-name {
    position: absolute; top: 112px; width: 100%; text-align: center;
    font-family: "Playfair Display", Georgia, serif;
    font-size: 22px; letter-spacing: 2px; color: var(--white);
  }

  .presents {
    position: absolute; top: 156px; left: 72px;
    font-family: "Kaushan Script", cursive;
    font-size: 28px; color: var(--gold);
  }

  .dancer-line {
    position: absolute; top: 200px; left: 188px; width: 452px; height: 315px;
    border-radius: 40% 40% 10% 10%;
    background: radial-gradient(ellipse at 50% 45%, rgba(20,10,50,.9) 0%, rgba(30,15,70,.75) 55%, transparent 80%);
  }

  .gold-swoosh { position: absolute; top: 610px; left: 56px; }

  .show-title {
    position: absolute; top: 500px; width: 100%; text-align: center;
    font-family: "Lobster", cursive; font-weight: 400;
    font-size: 176px; line-height: 1;
    color: var(--holiday-red);
    text-shadow: 0 0 2px var(--white), 2px 4px 0 #7a0a0c;
  }

  .show-subtitle {
    position: absolute; top: 706px; width: 100%; text-align: center;
    font-family: "Playfair Display", Georgia, serif; font-weight: 400;
    font-size: 54px; line-height: 1; letter-spacing: 2px; color: var(--white);
  }

  .credit-label {
    position: absolute; top: 784px; width: 100%; text-align: center;
    font-family: "Libre Baskerville", Georgia, serif; font-style: italic;
    font-size: 22px; line-height: 1; color: var(--gold);
  }

  .credit-name {
    position: absolute; top: 810px; width: 100%; text-align: center;
    font-family: "Oswald", sans-serif; font-weight: 700;
    font-size: 38px; line-height: 1.1; letter-spacing: 1px; color: var(--gold);
  }

  .ticket-line {
    position: absolute; top: 862px; width: 100%; text-align: center;
    font-family: "Oswald", sans-serif; font-weight: 700;
    font-size: 46px; line-height: 1.1; color: var(--white);
  }

  .venue-line, .contact-line {
    position: absolute; width: 100%; text-align: center;
    font-family: "Oswald", sans-serif; font-weight: 500; line-height: 1.1; color: var(--white);
  }
  .venue-line { top: 926px; font-size: 23px; }
  .contact-line { top: 958px; font-size: 19px; }

  .sponsor-strip {
    position: absolute; top: 994px; left: 24px; width: 705px; height: 62px;
    display: flex; align-items: center; gap: 12px;
  }
  .sponsor-label {
    font-family: "Libre Baskerville", Georgia, serif; font-style: italic;
    font-size: 14px; color: var(--gold); width: 72px; line-height: 1.1;
    white-space: normal !important;
  }
  .sponsor {
    flex: 1; height: 58px; padding: 0 6px;
    display: flex; align-items: center; justify-content: center;
    background: var(--white); color: var(--sponsor-dark);
    font-family: "Playfair Display", Georgia, serif; font-weight: 700;
    font-size: 16px; text-align: center; line-height: 1.15;
  }
</style>
</head>
<body>
<main class="poster">
  <div class="winter-backdrop" role="img" aria-label="Purple and blue winter sky filled with white snowflakes, fading to icy blue at the bottom"></div>

  <div class="academy-mark">PelMUSE Academy</div>
  <p class="company-name">PELMUSE BROADWAY COMPANY</p>
  <p class="presents">Presents...</p>

  <div class="dancer-line" role="img" aria-label="Line of silhouetted high-kick dancers in a V formation"></div>

  <svg class="gold-swoosh" width="640" height="90" viewBox="0 0 640 90" aria-hidden="true">
    <defs>
      <linearGradient id="swoosh-gold" x1="0" x2="1">
        <stop offset="0" stop-color="#c98a12" stop-opacity="0"/>
        <stop offset=".3" stop-color="#f3c13a"/>
        <stop offset=".7" stop-color="#f3c13a"/>
        <stop offset="1" stop-color="#c98a12" stop-opacity="0"/>
      </linearGradient>
    </defs>
    <path d="M0 70 Q320 10 640 60 L640 76 Q320 30 0 86 Z" fill="url(#swoosh-gold)"/>
  </svg>

  <h1 class="show-title">Holiday</h1>
  <h2 class="show-subtitle">EXTRAVAGANZA</h2>

  <p class="credit-label">Directed and Choreographed by</p>
  <p class="credit-name">COLIN ASHBY</p>

  <p class="ticket-line">TICKETS $$ • DECEMBER 12-13, 2015</p>
  <p class="venue-line">LYLE &amp; RUTH DANVERS THEATRE, 4817 Quillberry Bend, Lakeway, TX</p>
  <p class="contact-line">PelMUSE contact info | www.pel-muse.example and 555-307-4162 ext 204</p>

  <section class="sponsor-strip">
    <p class="sponsor-label">Sponsored by:</p>
    <div class="sponsor">Neva Orr Photography</div>
    <div class="sponsor">Pruitt Dentistry</div>
    <div class="sponsor">Bluefin Grill</div>
    <div class="sponsor">Up Tempo</div>
  </section>
</main>
</body>
</html>
```